Silver Ridge Business Card Design

I have an existing corporate logo. I'd like to clean it up bit (sharpen it up) and make it look better (without major redesign). I'd like to get the logo itself in all major file formats for print, web, etc.
Then I'd like a business card design that reflects a strategy consulting firm. It should be clean - logo and text without major graphics, and perhaps some small color treatments that match the logo color. The card should suggest high quality in terms of the company.
I'd like the files for card in all major print formats.
Target Market(s)
Silver Ridge Partners is a strategy development and business consulting firm focused on small to mid-sized companies. We specialize in business strategy, comprehensive business plan development, market segmentation and positioning, financial models, marketing and sales strategy, product strategy and the effective use of social media in business growth. We operate as consultants, advisers, retained members of management teams, and Board members. We often serve in the role of Chief Strategy Officer, supporting CEO's and other senior executives to enhance top and bottom line growth.
Our overall approach with clients is to deliver actual results, and we often take an active team role with business founders and management teams to drive business growth and affect real changes in performance. As a result, we approach each situation uniquely and partner with clients in a manner that will have the biggest impact on enterprise value.
Business
Look and feel

```html
<!DOCTYPE html>
<html lang="en">
<head>
<meta charset="utf-8">
<title>Silver Ridge Partners – Business Card</title>
<link rel="stylesheet" href="https://fonts.googleapis.com/css2?family=Jost:wght@300;400;500&display=swap">
<style>
  :root {
    --backdrop: #e2e2e2;
    --paper: #ffffff;
    --navy: #27335a;
    --taupe: #7d746c;
    --crop: #555555;
  }
  html, body {
    margin: 0;
    padding: 0;
    width: 1200px;
    height: 807px;
    overflow: hidden;
    background: var(--backdrop);
    font-family: "Jost", "Futura", sans-serif;
  }
  .sheet {
    position: absolute;
    left: 45px;
    top: 28px;
    width: 1108px;
    height: 731px;
    background: var(--paper);
    box-shadow: 0 1px 4px rgba(0,0,0,0.25);
  }
  .crop-marks {
    position: absolute;
    left: 0;
    top: 0;
    width: 1200px;
    height: 807px;
  }
  .brand {
    position: absolute;
    left: 208px;
    top: 196px;
    display: flex;
    align-items: center;
    gap: 18px;
    color: var(--navy);
  }
  .brand-dot {
    width: 58px;
    height: 58px;
    border-radius: 50%;
    background: var(--navy);
  }
  .brand-name {
    font-size: 25px;
    font-weight: 500;
    letter-spacing: 2px;
    line-height: 30px;
    text-transform: uppercase;
  }
  .person {
    position: absolute;
    right: 208px;
    top: 180px;
    text-align: right;
  }
  .person-name {
    margin: 0;
    font-size: 41px;
    font-weight: 400;
    line-height: 48px;
    color: var(--navy);
    letter-spacing: 0.5px;
  }
  .person-title {
    margin: 0;
    font-size: 31px;
    font-weight: 300;
    line-height: 40px;
    color: var(--taupe);
  }
  .website {
    position: absolute;
    left: 0;
    width: 1200px;
    top: 364px;
    text-align: center;
    font-size: 40px;
    font-weight: 500;
    color: var(--navy);
    letter-spacing: 0.5px;
  }
  .contact {
    position: absolute;
    font-size: 22px;
    font-weight: 300;
    line-height: 31px;
    color: var(--taupe);
  }
  .contact p { margin: 0; }
  .contact .label { color: var(--navy); font-weight: 500; }
  .address { left: 191px; top: 483px; }
  .direct-lines { left: 191px; top: 553px; }
  .social-lines { left: 640px; top: 553px; }
</style>
</head>
<body>
  <div class="sheet"></div>

  <svg class="crop-marks" width="1200" height="807" viewBox="0 0 1200 807" aria-hidden="true">
    <g stroke="var(--crop)" stroke-width="1">
      <line x1="159.5" y1="28" x2="159.5" y2="119"/>
      <line x1="1037.5" y1="28" x2="1037.5" y2="119"/>
      <line x1="159.5" y1="665" x2="159.5" y2="759"/>
      <line x1="1037.5" y1="665" x2="1037.5" y2="759"/>
      <line x1="45" y1="142.5" x2="139" y2="142.5"/>
      <line x1="1059" y1="142.5" x2="1153" y2="142.5"/>
      <line x1="45" y1="643.5" x2="139" y2="643.5"/>
      <line x1="1059" y1="643.5" x2="1153" y2="643.5"/>
    </g>
  </svg>

  <div class="brand">
    <span class="brand-dot"></span>
    <span class="brand-name">Silver Ridge<br>Partners</span>
  </div>

  <div class="person">
    <h1 class="person-name">Daniel M. Hartwell</h1>
    <p class="person-title">Partner and Founder</p>
  </div>

  <div class="website">www.srpartners.com</div>

  <div class="contact address">
    <p>412 Maple Crest Drive</p>
    <p>Lindenwood, Illinois 60499</p>
  </div>

  <div class="contact direct-lines">
    <p><span class="label">Direct:</span> 312.555.0147</p>
    <p><span class="label">Email:</span> daniel@srpartners.com</p>
  </div>

  <div class="contact social-lines">
    <p><span class="label">Network:</span> profiles.net/in/dhartwell/</p>
    <p><span class="label">Social:</span> @DanHartwell</p>
  </div>
</body>
</html>
```